New telco company needs a product page

We need to design two pages - one index and one inner.

We are a new telco company and we have developed our own phone. We will be selling our services and the phone on this site.

The design should be easy to understand and use, following the latest trends in Web design, be clean. It should communicate professionalism and integrity.

The name of our company is VORO which stands for Values Open Routes Onward. The design should follow this principle.

Our company logo is attached. I can send it in other colors/sizes - let me know.

Target Market(s)

Aging population (70+), middle-aged with parents and grandparents.

Industry/Entity Type

It Company

Requirements
Must have
• index page, inner page, flat, clean, Panelo 7 style / ZEB style (zebtrov.com), easy navigation, fluid layout, CSS, tableless
Should not have
• should not use old fonts, should not use old-style design, should not have animation, should not look like QRT or Gubble (too busy)

```html
<!DOCTYPE html>
<html lang="en">
<head>
<meta charset="utf-8">
<title>VORO — smart 2.01</title>
<link rel="stylesheet" href="https://fonts.googleapis.com/css2?family=Roboto+Condensed:wght@300;400&family=Open+Sans:wght@400;600&display=swap">
<style>
  :root {
    --header-top: #2b2e31;
    --header-bottom: #1d1f21;
    --nav-light: #d9d9d9;
    --nav-dark: #a9a9a9;
    --nav-active-light: #8d8d8d;
    --nav-active-dark: #5f5f5f;
    --nav-divider: #8a8a8a;
    --hero-center: #ffffff;
    --hero-edge: #cfd0d6;
    --ink: #2b2b2b;
    --ink-soft: #555555;
    --accent: #4e8a06;
    --btn-top: #86bb12;
    --btn-bottom: #3f7a04;
    --footer: #1f2022;
    --footer-line: #3a3c3f;
    --footer-text: #9a9a9a;
    --white: #ffffff;
  }
  * { margin: 0; padding: 0; box-sizing: border-box; }
  html, body { width: 1200px; height: 675px; overflow: hidden; }
  body { position: relative; font-family: "Roboto Condensed", Arial, sans-serif; background: var(--footer); }

  .site-header {
    position: absolute; left: 0; top: 0; width: 1200px; height: 156px;
    background: linear-gradient(var(--header-top), var(--header-bottom));
  }
  .brand {
    position: absolute; left: 524px; top: 36px; width: 150px; height: 70px;
    display: flex; align-items: center; gap: 10px;
    color: var(--white); font-weight: 300; font-size: 58px; letter-spacing: 1px; line-height: 1;
  }
  .brand-dot { width: 14px; height: 14px; border-radius: 50%; background: #bdbdbd; margin-top: 8px; }

  .main-nav {
    position: absolute; left: 314px; top: 126px; width: 564px; height: 30px;
    display: flex; background: linear-gradient(var(--nav-light), var(--nav-dark));
    border-radius: 2px 2px 0 0; font-family: "Open Sans", Arial, sans-serif; font-size: 11px;
  }
  .nav-item {
    display: flex; align-items: center; justify-content: center; height: 100%;
    color: #2a2a2a; text-decoration: none; border-right: 1px solid var(--nav-divider);
    text-shadow: 0 1px 0 rgba(255,255,255,.5);
  }
  .nav-home { width: 86px; }
  .nav-about { width: 101px; background: linear-gradient(var(--nav-active-light), var(--nav-active-dark)); color: var(--white); text-shadow: 0 1px 1px rgba(0,0,0,.4); }
  .nav-products { width: 104px; }
  .nav-shop { width: 101px; }
  .nav-search { flex: 1; display: flex; align-items: center; padding-left: 28px; }
  .search-field {
    width: 112px; height: 18px; border-radius: 9px; background: linear-gradient(#f4f4f4, #e2e2e2);
    border: 1px solid #9a9a9a; display: flex; align-items: center; gap: 4px; padding-left: 5px;
    color: #666; font-size: 10px;
  }

  .hero {
    position: absolute; left: 0; top: 156px; width: 1200px; height: 441px;
    background: radial-gradient(ellipse 620px 300px at 540px 230px, var(--hero-center) 30%, var(--hero-edge) 100%);
    border-top: 1px solid #8d8f93;
  }
  .hero-copy { position: absolute; left: 321px; top: 120px; width: 300px; color: var(--ink); }
  .product-name { font-weight: 300; font-size: 22px; line-height: 26px; }
  .product-tagline { font-weight: 400; font-size: 18px; line-height: 24px; }
  .product-tagline em { font-style: normal; color: var(--accent); }
  .product-text { margin-top: 6px; font-weight: 300; font-size: 14px; line-height: 19.5px; color: var(--ink-soft); }
  .order-button {
    position: absolute; left: 0; top: 139px; width: 186px; height: 53px;
    display: flex; align-items: center; justify-content: center; gap: 10px;
    background: linear-gradient(var(--btn-top), var(--btn-bottom));
    color: var(--white); font-weight: 300; font-size: 24px; text-decoration: none;
    box-shadow: 2px 3px 4px rgba(0,0,0,.3); text-shadow: 0 1px 2px rgba(0,0,0,.35);
  }
  .product-visual {
    position: absolute; left: 650px; top: 50px; width: 233px; height: 352px;
    border-radius: 24px; background: linear-gradient(135deg, #e9ecef, #8fb4dc 45%, #3c3f44);
  }
  .slide-arrow { position: absolute; top: 200px; }
  .slide-prev { left: 35px; }
  .slide-next { left: 1142px; }

  .site-footer {
    position: absolute; left: 0; top: 597px; width: 1200px; height: 78px;
    background: var(--footer); border-top: 2px solid var(--footer-line);
    color: var(--footer-text); font-size: 13px;
  }
  .copyright { position: absolute; left: 321px; top: 30px; }
  .social { position: absolute; right: 322px; top: 30px; display: flex; gap: 10px; }
</style>
</head>
<body>
  <header class="site-header">
    <div class="brand"><span>voro</span><span class="brand-dot"></span></div>
    <nav class="main-nav">
      <a class="nav-item nav-home" href="#" aria-label="Home">
        <svg width="18" height="16" viewBox="0 0 18 16"><path d="M9 1 L17 8 H14.5 V15 H11 V10.5 H7 V15 H3.5 V8 H1 Z" fill="#f2f2f2" stroke="#6d6d6d" stroke-width="1"/></svg>
      </a>
      <a class="nav-item nav-about" href="#">About</a>
      <a class="nav-item nav-products" href="#">Products</a>
      <a class="nav-item nav-shop" href="#">Shop</a>
      <div class="nav-search">
        <div class="search-field">
          <svg width="9" height="9" viewBox="0 0 9 9"><circle cx="3.6" cy="3.6" r="2.7" fill="none" stroke="#555" stroke-width="1.2"/><path d="M5.6 5.6 L8.4 8.4" stroke="#555" stroke-width="1.4"/></svg>
          <span>Search</span>
        </div>
      </div>
    </nav>
  </header>

  <main class="hero">
    <svg class="slide-arrow slide-prev" width="22" height="46" viewBox="0 0 22 46"><path d="M20 2 L3 23 L20 44" fill="none" stroke="#a4a6ab" stroke-width="2.5"/></svg>

    <section class="hero-copy">
      <h1 class="product-name">voro smart 2.01</h1>
      <h2 class="product-tagline"><em>unleash</em> your dream</h2>
      <p class="product-text">Lorem ipsum dolor sit amet, consectetur adipisicing elit, sed do eiusmod tempor incididunt ut labore et dolore magna aliqua.</p>
      <a class="order-button" href="#">Order Now
        <svg width="12" height="14" viewBox="0 0 12 14"><path d="M1 1 L6 7 L1 13 M6 1 L11 7 L6 13" fill="none" stroke="#fff" stroke-width="1.6"/></svg>
      </a>
    </section>

    <div class="product-visual" role="img" aria-label="Two voro smart 2.01 phones, white and black, showing the home screen"></div>

    <svg class="slide-arrow slide-next" width="22" height="46" viewBox="0 0 22 46"><path d="M2 2 L19 23 L2 44" fill="none" stroke="#a4a6ab" stroke-width="2.5"/></svg>
  </main>

  <footer class="site-footer">
    <p class="copyright">Copyright@2013, voro</p>
    <p class="social"><span>Follow Us :</span><span>Pipbird</span><span>Brooknet</span></p>
  </footer>
</body>
</html>
```